Business Card Design

Motorvane Ledger is an online automotive resource on a national scale specifically targeting lease purchases for new cars. Our Online and app platform allow prospective lease clients to scan a window sticker while at a franchise dealership and instantly receive a lease quote at what we call the sweet spot. Motorvane Ledger offers price transparency during the lease process to allow average people the confidence in the lease process and takes away any fear of the big franchise dealers.
Motorvane ledger allows ordinary lease customers to know they are getting a low price lease and not overpaying. Never overpay again

Industry/Entity Type

Automotive

Contact Information for Business Card

Motorvane Ledger
Martin Sowerby (President of operations)
Phone: 888-247-6031
Cell: 561-384-2706

```html
<!DOCTYPE html>
<html lang="en">
<head>
<meta charset="utf-8">
<title>Motorvane Ledger — Business Card</title>
<link rel="stylesheet" href="https://fonts.googleapis.com/css2?family=Montserrat:wght@800&family=Courgette&family=Open+Sans:wght@400&display=swap">
<style>
  :root {
    --ink: #0a0a0a;
    --paper: #f7f7f4;
    --backdrop: #8d8d8d;
    --muted: #d8d8d8;
  }
  * { box-sizing: border-box; margin: 0; padding: 0; }
  html, body { width: 1200px; height: 1200px; overflow: hidden; }
  body {
    background: var(--backdrop);
    position: relative;
    font-family: "Open Sans", sans-serif;
  }
  .card {
    position: absolute;
    left: 150px;
    width: 900px;
    height: 514px;
    background: var(--paper);
    overflow: hidden;
    box-shadow: 0 6px 18px rgba(0,0,0,0.25);
  }
  .card--front { top: 60px; }
  .card--back { top: 626px; }
  .card__art { position: absolute; inset: 0; }
  .brand {
    position: absolute;
    display: flex;
    align-items: center;
    gap: 22px;
  }
  .brand__mark {
    background: var(--ink);
    flex: none;
  }
  .brand__name {
    font-family: "Montserrat", sans-serif;
    font-weight: 800;
    text-transform: uppercase;
    color: var(--ink);
    line-height: 0.95;
    letter-spacing: -1px;
  }
  .card--front .brand { left: 190px; top: 110px; }
  .card--front .brand__mark { width: 70px; height: 70px; }
  .card--front .brand__name { font-size: 80px; }
  .card--back .brand { left: 300px; top: 36px; }
  .card--back .brand__mark { width: 46px; height: 46px; }
  .card--back .brand__name { font-size: 54px; }
  .holder {
    position: absolute;
    left: 430px;
    top: 268px;
    width: 380px;
    text-align: center;
    color: var(--paper);
  }
  .holder__name {
    font-family: "Courgette", cursive;
    font-size: 32px;
  }
  .holder__title {
    font-size: 12px;
    color: var(--muted);
    margin-top: 2px;
  }
  .contacts {
    position: absolute;
    left: 520px;
    top: 392px;
    list-style: none;
    color: var(--paper);
    font-size: 22px;
    letter-spacing: 1px;
  }
  .contacts__item {
    display: flex;
    align-items: center;
    gap: 22px;
    height: 46px;
  }
  .contacts__icon { width: 22px; height: 22px; flex: none; }
</style>
</head>
<body>

<section class="card card--front" aria-label="Card front">
  <svg class="card__art" viewBox="0 0 900 514" aria-hidden="true">
    <g class="road-dashes" fill="#0a0a0a">
      <rect x="10" y="282" width="52" height="8"/>
      <rect x="100" y="282" width="52" height="8"/>
      <rect x="190" y="282" width="52" height="8"/>
      <rect x="280" y="282" width="52" height="8"/>
      <rect x="370" y="282" width="52" height="8"/>
      <rect x="460" y="282" width="52" height="8"/>
      <rect x="550" y="282" width="52" height="8"/>
      <rect x="640" y="282" width="52" height="8"/>
      <rect x="730" y="282" width="52" height="8"/>
      <rect x="820" y="282" width="52" height="8"/>
    </g>
    <rect class="road-band" x="0" y="300" width="900" height="214" fill="#0a0a0a"/>
  </svg>
  <div class="brand">
    <span class="brand__mark"></span>
    <span class="brand__name">Motorvane<br>Ledger</span>
  </div>
</section>

<section class="card card--back" aria-label="Card back">
  <svg class="card__art" viewBox="0 0 900 514" aria-hidden="true">
    <g class="road-dashes" fill="#0a0a0a">
      <rect x="0" y="148" width="40" height="6"/>
      <rect x="70" y="148" width="40" height="6"/>
      <rect x="140" y="148" width="40" height="6"/>
      <rect x="210" y="148" width="40" height="6"/>
      <rect x="280" y="148" width="40" height="6"/>
      <rect x="350" y="148" width="40" height="6"/>
      <rect x="420" y="148" width="40" height="6"/>
    </g>
    <polygon class="road-band" points="0,164 470,164 548,236 900,236 900,514 0,514" fill="#0a0a0a"/>
    <line class="divider" x1="0" y1="352" x2="900" y2="352" stroke="#f7f7f4" stroke-width="2"/>
  </svg>
  <div class="brand">
    <span class="brand__mark"></span>
    <span class="brand__name">Motorvane<br>Ledger</span>
  </div>
  <div class="holder">
    <p class="holder__name">Martin Sowerby</p>
    <p class="holder__title">(President of operations)</p>
  </div>
  <ul class="contacts">
    <li class="contacts__item">
      <svg class="contacts__icon" viewBox="0 0 22 22" aria-hidden="true">
        <circle cx="11" cy="11" r="7" fill="none" stroke="#f7f7f4" stroke-width="2"/>
        <circle cx="11" cy="11" r="2.5" fill="#f7f7f4"/>
        <path d="M11 0v5M11 17v5M0 11h5M17 11h5" stroke="#f7f7f4" stroke-width="2"/>
      </svg>
      <span>Phone: 888-247-6031</span>
    </li>
    <li class="contacts__item">
      <svg class="contacts__icon" viewBox="0 0 22 22" aria-hidden="true">
        <circle cx="11" cy="11" r="7" fill="none" stroke="#f7f7f4" stroke-width="2"/>
        <circle cx="11" cy="11" r="2.5" fill="#f7f7f4"/>
        <path d="M11 0v5M11 17v5M0 11h5M17 11h5" stroke="#f7f7f4" stroke-width="2"/>
      </svg>
      <span>Cell: 561-384-2706</span>
    </li>
  </ul>
</section>

</body>
</html>
```